3 screens for iOS app

I need a settings screen, dashboard and leaderboard screen created for an iPhone fitness app that is nearing completion. I have the template in .psd format that needs to be adhered to for consistency, and there are wireframe sketches (literally pen & paper) that you will translate into .psd files for chopping up and adding into the app. Also I need this by Monday.

Settings Screen:

Using the template psd, I need a basic list similar to the setting screen example attached (no icons needed, just text). The list of settings in order are:
Disclaimer
Edit Profile
Feedback
Help!
Terms of Use
Privacy Policy
Push Notifications (switcher icon on/off)
Chatterly Posts (switcher icon on/off)
Quipster Posts (switcher icon on/off)
Zenvok Videos Channel
Log Out

Dashboard:
The dashboard tempalte is attached. This dashboard should be inserted between the Grey banner heading and the Orange 14min standard routine bar. It will shift the graph down. The graph should remain unchanged, all you need to do in sert a cool looking dashboard inbetween the grey and orange bars

Dashboard contents:

Three dials (similar to pulsora, stridewell etc - see attached as an example) that display your progress

Dial 1: Title: Week
Dial should change colour as score approaches goal (ideally from green to orange as per icon example attached but not necessarily if you can make it look better)
Inside the dial it needs to include
Total: 598
Goal: 2,000
Days left: 5

Dial 2: Title: Improvement
Inside the dial it needs to include:
Start: 350
PB: 700
+100% in bold, centered

Dial 3: Title: Belt
Inside the dial needs to include:
Total: 9,834
Goal: 25,000

Leaderboard Screen:

Again using the template, with the grey banner heading at the top and tab bar at the bottom:

The leaderboard should be divided into two sections. The first is for my personal scores (as a user). The second section is for all players scores.

Section 1:
- Light grey background, dark grey text. Column titles can be pressed to filter columns. When pressed title changes colour from grey to orange (bold). If you can highlight two of the column titles orange that will be good

Section 2:
- White background, dark grey text. Column titles can be pressed to filter columns.
- Row height should be quite small to fit a large number of names on the screen.

Column titles: (sorry the wireframe sketch text is tough to read)
Rank / Name / W/outs / Wins / Week / Total / Belt

Rank - numeric values from 1-999
Name - text field
W/outs - number from 1-999
Wins - number 1-999
Week - number 1 - 99,999
Total - number 1- 99,999
Belt - coloured dot (white, black, red, blue, green, yellow)

For more info, refer http://www.zenvok.example/ and download the old app (iphone only) for an idea what we're after.

Industry/Entity Type

Fitness

Colors
f68e4e

Requirements
Must have
• Use the .psd template provided. We're not looking for a redesign.
• The fonts are:
• LeckerliOne Regular
• LobsterTwo Bold
• MeriendaOne Regular
• MVBoli
• GothamExtraLight
• LobsterTwo
Nice to have
• The best dashboard of all time.
Should not have
• changes to fonts,

```html
<!DOCTYPE html>
<html lang="en">
<head>
<meta charset="utf-8">
<title>Zenvok – Dashboard, Leader Board, Settings</title>
<link rel="stylesheet" href="https://fonts.googleapis.com/css2?family=Bebas+Neue&family=Open+Sans:wght@400;600&display=swap">
<style>
  :root {
    --orange: #f68e4e;
    --orange-deep: #ff6a14;
    --green: #7cc43a;
    --dark: #3b3b3b;
    --panel: #4a4a4a;
    --ink: #333333;
    --muted: #8a8a8a;
    --rule: #ececec;
    --white: #ffffff;
    --page: #f3f3f3;
    --bar: #d9d9d9;
    --switch-off: #d4d4d4;
  }
  * { box-sizing: border-box; margin: 0; padding: 0; }
  html, body { width: 1200px; height: 675px; overflow: hidden; }
  body { background: var(--page); position: relative; font-family: "Open Sans", sans-serif; color: var(--ink); }

  .screen {
    position: absolute; top: 125px; width: 254px; height: 451px;
    transform: scale(0.878); transform-origin: top left;
    background: var(--white); overflow: hidden;
  }
  .screen--dashboard { left: 84px; }
  .screen--leaderboard { left: 498px; }
  .screen--settings { left: 907px; }

  .app-header {
    position: absolute; top: 0; left: 0; right: 0; height: 37px;
    background: var(--orange); color: var(--white);
    display: flex; align-items: center; justify-content: center;
    font-size: 11.5px;
  }
  .app-header .gear { position: absolute; left: 6px; top: 9px; width: 19px; height: 19px; }
  .app-header .brand { font-weight: 600; font-size: 13px; }

  /* Dashboard */
  .hero-photo {
    position: absolute; top: 37px; left: 0; right: 0; height: 374px;
    background: linear-gradient(160deg, #e9e6e2 0%, #cfc8bf 35%, #a89f93 60%, #8d8378 100%);
  }
  .dial {
    position: absolute; top: 15px; width: 78px; height: 78px; border-radius: 50%;
    border: 2px solid var(--orange); background: rgba(255,255,255,0.88);
    display: flex; flex-direction: column; align-items: center; justify-content: center;
    font-family: "Bebas Neue", sans-serif; font-size: 12.5px; line-height: 1.02; color: #222;
  }
  .dial--week { left: 2px; }
  .dial--improvement { left: 88px; }
  .dial--belt { left: 174px; background: rgba(255,255,255,0.7); }
  .dial .dial-big { font-size: 18px; }
  .dial-title {
    position: absolute; top: 98px; width: 86px; text-align: center;
    font-family: "Bebas Neue", sans-serif; font-size: 13px; color: #222;
  }
  .routine-bar {
    position: absolute; top: 121px; left: 0; right: 0; height: 48px;
    background: rgba(150,140,130,0.85); color: var(--white);
    font-family: "Bebas Neue", sans-serif; font-size: 15px;
    display: flex; align-items: center; padding-left: 54px;
  }
  .routine-bar .clock { position: absolute; left: 2px; top: 3px; width: 42px; height: 42px; }
  .routine-bar::after {
    content: ""; position: absolute; left: 120px; bottom: -6px;
    border-left: 6px solid transparent; border-right: 6px solid transparent;
    border-top: 6px solid rgba(150,140,130,0.85);
  }
  .chart { position: absolute; top: 180px; left: 0; width: 254px; height: 190px; }

  /* Tab bar */
  .tab-bar {
    position: absolute; bottom: 0; left: 0; right: 0; height: 40px;
    background: var(--dark); display: flex;
  }
  .tab { flex: 1; color: #c9c9c9; font-size: 7px; text-align: center; padding-top: 4px; position: relative; }
  .tab svg { display: block; margin: 0 auto 1px; width: 20px; height: 20px; }
  .tab--active { color: var(--white); }
  .tab--start {
    color: var(--white); background: var(--orange-deep);
    border-radius: 30px 30px 0 0; margin-top: -8px; padding-top: 8px;
  }
  .tab .badge {
    position: absolute; top: 2px; left: 50%; margin-left: -5px; width: 11px; height: 11px;
    border-radius: 50%; background: var(--orange); color: var(--white); font-size: 7px; line-height: 11px;
  }

  /* Stats panel */
  .stats {
    position: absolute; left: 0; right: 0; height: 58px; background: var(--panel);
    font-family: "Bebas Neue", sans-serif; font-size: 10px; line-height: 10px;
  }
  .stats .stat { position: absolute; display: flex; }
  .stats .label { color: var(--orange); width: 50px; }
  .stats .colon { color: var(--white); width: 17px; }
  .stats .value { color: var(--white); }
  .stats .right .label { width: 72px; }
  .stats .right .colon { width: 33px; }
  .stats .right .value { width: 20px; text-align: right; }
  .dot { display: inline-block; width: 7px; height: 7px; border-radius: 50%; }

  /* Leader board */
  .board { position: absolute; top: 95px; left: 0; right: 0; bottom: 40px; font-size: 7.5px; }
  .board-row { position: absolute; left: 0; right: 0; display: grid;
    grid-template-columns: 31px 35px 41px 31px 35px 37px 30px; padding-left: 10px; align-items: center; }
  .board-row span:nth-child(n+3):nth-child(-n+6) { text-align: right; padding-right: 6px; }
  .board-row span:last-child { text-align: center; }
  .board-head { color: var(--orange); }
  .dot--white { border: 1px solid #aaa; background: var(--white); }

  /* Settings */
  .profile-band {
    position: absolute; top: 37px; left: 0; right: 0; height: 85px;
    background: linear-gradient(100deg, #5b6a78 0%, #8a4a4a 45%, #c0392b 62%, #6d4a52 100%);
  }
  .avatar {
    position: absolute; left: 15px; top: 15px; width: 62px; height: 62px; border-radius: 50%;
    border: 2px solid var(--white); background: linear-gradient(160deg, #9fb6c6, #6f8696);
  }
  .profile-name { position: absolute; left: 86px; top: 35px; color: var(--white);
    font-family: "Bebas Neue", sans-serif; font-size: 19px; }
  .settings-list { position: absolute; top: 186px; left: 0; right: 0; list-style: none; }
  .settings-item { height: 23.5px; display: flex; align-items: center; justify-content: space-between;
    padding: 0 14px 0 18px; font-size: 9.5px; color: #555; border-bottom: 1px solid var(--rule); }
  .switch { width: 24px; height: 13px; border-radius: 7px; background: var(--switch-off); position: relative; }
  .switch::after { content: ""; position: absolute; top: 1px; left: 1px; width: 11px; height: 11px;
    border-radius: 50%; background: var(--white); }
  .switch--on { background: var(--orange); }
  .switch--on::after { left: 12px; }
</style>
</head>
<body>

<svg width="0" height="0" style="position:absolute">
  <defs>
    <symbol id="gear" viewBox="0 0 24 24"><circle cx="12" cy="12" r="3.5" fill="none" stroke="#fff" stroke-width="1.6"/><path d="M12 2.5v3M12 18.5v3M2.5 12h3M18.5 12h3M5.3 5.3l2.1 2.1M16.6 16.6l2.1 2.1M5.3 18.7l2.1-2.1M16.6 7.4l2.1-2.1" stroke="#fff" stroke-width="1.6" stroke-linecap="round"/><circle cx="12" cy="12" r="7" fill="none" stroke="#fff" stroke-width="1.6"/></symbol>
    <symbol id="person" viewBox="0 0 24 24"><circle cx="12" cy="8" r="4.5" fill="none" stroke="currentColor" stroke-width="1.4"/><path d="M3.5 22c0-5 3.8-8 8.5-8s8.5 3 8.5 8z" fill="none" stroke="currentColor" stroke-width="1.4"/></symbol>
    <symbol id="trend" viewBox="0 0 24 24"><path d="M2 20l6-7 4 4 5-8 5 3" fill="none" stroke="#7cc43a" stroke-width="2"/><path d="M2 16l6-7 4 4 5-8 5 3" fill="none" stroke="#7cc43a" stroke-width="1.2"/></symbol>
    <symbol id="play" viewBox="0 0 24 24"><path d="M6 3l15 9-15 9z" fill="#fff"/></symbol>
    <symbol id="medal" viewBox="0 0 24 24"><circle cx="12" cy="9" r="6" fill="none" stroke="currentColor" stroke-width="1.4"/><path d="M8 14l-2 8 6-3 6 3-2-8" fill="none" stroke="currentColor" stroke-width="1.4"/></symbol>
    <symbol id="arm" viewBox="0 0 24 24"><path d="M3 20c2-6 4-9 7-12l2-4 4 1-2 3 2 2c3-1 5 1 5 4 0 4-4 6-9 6z" fill="none" stroke="currentColor" stroke-width="1.4" stroke-linejoin="round"/></symbol>
  </defs>
</svg>

<!-- Dashboard -->
<section class="screen screen--dashboard">
  <header class="app-header">
    <svg class="gear"><use href="#gear"/></svg>
    <span class="brand">Zenvok</span>
  </header>
  <div class="hero-photo" role="img" aria-label="Photo of an athlete training in a bright gym">
    <div class="dial dial--week"><span>Total:598</span><span>Goal:2,000</span><span>Days left:5</span></div>
    <div class="dial dial--improvement"><span>Start:350</span><span>PB:700</span><span class="dial-big">+100%</span></div>
    <div class="dial dial--belt"><span>Total:9,834</span><span>Goal:25,000</span></div>
    <div class="dial-title" style="left:0">Week</div>
    <div class="dial-title" style="left:84px">Improvement</div>
    <div class="dial-title" style="left:170px">Belt</div>

    <div class="routine-bar">
      <svg class="clock" viewBox="0 0 42 42"><circle cx="21" cy="21" r="20" fill="#fff"/><path d="M21 8v13h-9" fill="none" stroke="#222" stroke-width="1.5"/></svg>
      14:00 Minute Standard Routine
    </div>

    <svg class="chart" viewBox="0 0 254 190">
      <g font-family="Open Sans, sans-serif" font-size="4.5" fill="#555">
        <text x="24" y="12">600</text><text x="24" y="27">540</text><text x="24" y="42">480</text>
        <text x="24" y="57">420</text><text x="24" y="72">360</text><text x="24" y="87">300</text>
        <text x="24" y="102">240</text><text x="24" y="117">180</text><text x="24" y="132">120</text>
        <text x="24" y="147">60</text>
      </g>
      <g fill="var(--bar)">
        <rect x="40" y="79" width="18" height="84" rx="2"/>
        <rect x="69" y="63" width="18" height="100" rx="2"/>
        <rect x="123" y="93" width="18" height="70" rx="2"/>
        <rect x="150" y="53" width="18" height="110" rx="2"/>
        <rect x="177" y="26" width="18" height="137" rx="2"/>
        <rect x="204" y="7" width="18" height="156" rx="2"/>
      </g>
      <rect x="97" y="71" width="18" height="92" rx="2" fill="var(--green)"/>
      <circle cx="106" cy="74" r="8" fill="#fff" stroke="var(--orange)" stroke-width="1.5"/>
      <circle cx="106" cy="74" r="6" fill="var(--orange)"/>
      <text x="106" y="76.5" font-size="7" fill="#fff" text-anchor="middle" font-family="Open Sans, sans-serif">81</text>
      <line x1="30" y1="163" x2="231" y2="163" stroke="#eee" stroke-width="1"/>
    </svg>
  </div>
  <nav class="tab-bar">
    <div class="tab"><svg><use href="#person"/></svg>Profile</div>
    <div class="tab tab--active"><svg><use href="#trend"/></svg>Results</div>
    <div class="tab tab--start"><svg><use href="#play"/></svg>Start</div>
    <div class="tab"><span class="badge">2</span><svg><use href="#medal"/></svg>Challenges</div>
    <div class="tab"><svg><use href="#arm"/></svg>Routines</div>
  </nav>
</section>

<!-- Leader Board -->
<section class="screen screen--leaderboard">
  <header class="app-header">
    <svg class="gear"><use href="#gear"/></svg>
    <span>Leader Board</span>
  </header>
  <div class="stats" style="top:37px">
    <div class="stat" style="left:10px;top:14px"><span class="label">Rank</span><span class="colon">:</span><span class="value">999</span></div>
    <div class="stat" style="left:10px;top:24px"><span class="label">W/outs</span><span class="colon">:</span><span class="value">999</span></div>
    <div class="stat" style="left:10px;top:34px"><span class="label">Wins</span><span class="colon">:</span><span class="value">999</span></div>
    <div class="stat right" style="left:118px;top:14px"><span class="label">Week</span><span class="colon">:</span><span class="value">99,999</span></div>
    <div class="stat right" style="left:118px;top:24px"><span class="label">Total Number</span><span class="colon">:</span><span class="value">99,999</span></div>
    <div class="stat right" style="left:118px;top:34px"><span class="label">Belt</span><span class="colon">:</span><span class="value"><i class="dot" style="background:#e02020"></i></span></div>
  </div>
  <div class="board">
    <div class="board-row board-head" style="top:12px"><span>Rank</span><span>Name</span><span>W/outs</span><span>Wins</span><span>Week</span><span>Total</span><span>Belts</span></div>
    <div class="board-row" style="top:28px"><span>#1</span><span>Jhon</span><span>40</span><span>27</span><span>1,978</span><span>10,111</span><span><i class="dot" style="background:#f5c400"></i></span></div>
    <div class="board-row" style="top:54px"><span>#2</span><span>Mary</span><span>29</span><span>14</span><span>1,678</span><span>9,812</span><span><i class="dot" style="background:#22c322"></i></span></div>
    <div class="board-row" style="top:78px"><span>#3</span><span>Andrew</span><span>21</span><span>12</span><span>1,121</span><span>7,612</span><span><i class="dot" style="background:#1e5ee8"></i></span></div>
    <div class="board-row" style="top:104px"><span>#5</span><span>Jhon</span><span>40</span><span>27</span><span>1,978</span><span>10,111</span><span><i class="dot" style="background:#1e5ee8"></i></span></div>
    <div class="board-row" style="top:129px"><span>#6</span><span>Mary</span><span>29</span><span>14</span><span>1,678</span><span>9,812</span><span><i class="dot" style="background:#e02020"></i></span></div>
    <div class="board-row" style="top:153px"><span>#7</span><span>Andrew</span><span>21</span><span>12</span><span>1,121</span><span>7,612</span><span><i class="dot" style="background:#e02020"></i></span></div>
    <div class="board-row" style="top:177px"><span>#8</span><span>Jhon</span><span>40</span><span>27</span><span>1,978</span><span>10,111</span><span><i class="dot" style="background:#e02020"></i></span></div>
    <div class="board-row" style="top:200px"><span>#9</span><span>Mary</span><span>29</span><span>14</span><span>1,678</span><span>9,812</span><span><i class="dot" style="background:#111"></i></span></div>
    <div class="board-row" style="top:222px"><span>#10</span><span>Andrew</span><span>21</span><span>12</span><span>1,121</span><span>7,612</span><span><i class="dot dot--white"></i></span></div>
    <div class="board-row" style="top:244px"><span>#11</span><span>Jhon</span><span>40</span><span>27</span><span>1,978</span><span>10,111</span><span><i class="dot" style="background:#111"></i></span></div>
    <div class="board-row" style="top:264px"><span>#12</span><span>Mary</span><span>29</span><span>14</span><span>1,678</span><span>9,812</span><span><i class="dot dot--white"></i></span></div>
    <div class="board-row" style="top:286px"><span>#13</span><span>Andrew</span><span>21</span><span>12</span><span>1,121</span><span>7,612</span><span><i class="dot dot--white"></i></span></div>
  </div>
  <nav class="tab-bar">
    <div class="tab"><svg><use href="#person"/></svg>Profile</div>
    <div class="tab tab--active"><svg><use href="#trend"/></svg>Results</div>
    <div class="tab tab--start"><svg><use href="#play"/></svg>Start</div>
    <div class="tab"><span class="badge">2</span><svg><use href="#medal"/></svg>Challenges</div>
    <div class="tab"><svg><use href="#arm"/></svg>Routines</div>
  </nav>
</section>

<!-- Settings -->
<section class="screen screen--settings">
  <header class="app-header">
    <svg class="gear"><use href="#gear"/></svg>
    <span>Settings</span>
  </header>
  <div class="profile-band" role="img" aria-label="Blurred colourful backdrop behind the user profile">
    <div class="avatar" role="img" aria-label="User profile photo"></div>
    <div class="profile-name">Dale Marsh</div>
  </div>
  <div class="stats" style="top:122px">
    <div class="stat" style="left:10px;top:15px"><span class="label">Rank</span><span class="colon">:</span><span class="value">999</span></div>
    <div class="stat" style="left:10px;top:25px"><span class="label">W/outs</span><span class="colon">:</span><span class="value">999</span></div>
    <div class="stat" style="left:10px;top:35px"><span class="label">Wins</span><span class="colon">:</span><span class="value">999</span></div>
    <div class="stat right" style="left:118px;top:15px"><span class="label">Week</span><span class="colon">:</span><span class="value">99,999</span></div>
    <div class="stat right" style="left:118px;top:25px"><span class="label">Total Number</span><span class="colon">:</span><span class="value">99,999</span></div>
    <div class="stat right" style="left:118px;top:35px"><span class="label">Belt</span><span class="colon">:</span><span class="value"><i class="dot" style="background:#e02020"></i></span></div>
  </div>
  <ul class="settings-list">
    <li class="settings-item">Disclaimer</li>
    <li class="settings-item">Edit Profile</li>
    <li class="settings-item">Feedback</li>
    <li class="settings-item">Help!</li>
    <li class="settings-item">Terms of Use</li>
    <li class="settings-item">Privacy Policy</li>
    <li class="settings-item">Push Notifications<span class="switch switch--on"></span></li>
    <li class="settings-item">Chatterly Posts<span class="switch switch--on"></span></li>
    <li class="settings-item">Quipster Posts<span class="switch"></span></li>
    <li class="settings-item">Zenvok Videos Channel</li>
    <li class="settings-item">Log Out</li>
  </ul>
</section>

</body>
</html>
```